Wine label design for my wife. Wine called "The Mirabel"

I need a wine label face lift of one of my premium wines in my collection. My wine sells in Harbor Lark's all over the States. My current label is called The Mirabel (my wife's name) and the illustration of her eyes is done by a well know artist from South Africa. I do not have to use this illustration and therefor I attached several pictures of her and her eyes, even when she was a little girl. The wine's also made in South Africa. This is a premium wine that we only sell 2000 bottles per year. The wine sells at 60 usd per bottle, The current label is too white. I also think her eyes should look more at the person buying it, than away from them.

Target Market(s)

Top end wine buyers

Font styles to use
Decorative
Script

Requirements
Must have
• 'The Mirabel' must be on the label
An illustration must be on the label
Basically all the info that's on the current label must be on by law. As per Sample
Nice to have
• Maybe some ideas of her whole face?
Should not have
• any gold colour

```html
<!DOCTYPE html>
<html lang="en">
<head>
<meta charset="utf-8">
<title>The Mirabel — Sauvignon 2017 Label</title>
<link href="https://fonts.googleapis.com/css2?family=Pinyon+Script&family=Cormorant+Garamond:wght@400;500&display=swap" rel="stylesheet">
<style>
  :root {
    --backdrop: #142033;
    --label-light: #e4e5e8;
    --label-mid: #cdcfd3;
    --label-shade: #b3b6bc;
    --title-ink: #fbfbfc;
    --varietal-ink: #6c6f76;
    --art-light: #f3f4f6;
    --art-edge: #c2c5cb;
    --signature-tone: #d9dbdf;
  }
  * { margin: 0; padding: 0; box-sizing: border-box; }
  html, body {
    width: 1200px;
    height: 1200px;
    overflow: hidden;
    background: var(--backdrop);
  }
  .canvas {
    position: relative;
    width: 1200px;
    height: 1200px;
    display: flex;
    align-items: center;
    justify-content: center;
  }
  .wine-label {
    position: relative;
    width: 920px;
    height: 890px;
    background: linear-gradient(100deg, var(--label-shade) 0%, var(--label-mid) 25%, var(--label-light) 65%, var(--label-light) 100%);
    overflow: hidden;
  }
  .wine-name {
    position: absolute;
    left: 0;
    top: 350px;
    width: 668px;
    text-align: center;
    font-family: "Pinyon Script", cursive;
    font-weight: 400;
    font-size: 140px;
    line-height: 1;
    white-space: nowrap;
    color: var(--title-ink);
    text-shadow: 0 1px 2px rgba(90, 94, 102, 0.4);
  }
  .varietal {
    position: absolute;
    left: 70px;
    top: 505px;
    font-family: "Cormorant Garamond", serif;
    font-weight: 500;
    font-size: 56px;
    line-height: 1;
    letter-spacing: 2px;
    white-space: nowrap;
    color: var(--varietal-ink);
  }
  .signature-art {
    position: absolute;
    left: 70px;
    top: 760px;
    width: 200px;
    height: 70px;
  }
  .portrait-art {
    position: absolute;
    right: 0;
    top: 0;
    width: 240px;
    height: 100%;
  }
</style>
</head>
<body>
  <main class="canvas">
    <section class="wine-label">
      <h1 class="wine-name">The Mirabel</h1>
      <p class="varietal">SAUVIGNON 2017</p>

      <svg class="signature-art" viewBox="0 0 200 70" role="img" aria-label="Winemaker's handwritten signature">
        <rect x="0" y="0" width="200" height="70" rx="6" fill="var(--signature-tone)"/>
      </svg>

      <svg class="portrait-art" viewBox="0 0 240 890" role="img" aria-label="Embossed white line portrait of Mirabel, the winemaker's wife, looking toward the viewer">
        <path d="M240 0 L120 0 C80 120 70 260 60 400 C50 560 40 700 20 890 L240 890 Z"
              fill="var(--art-light)" stroke="var(--art-edge)" stroke-width="2"/>
      </svg>
    </section>
  </main>
</body>
</html>
```